K&R Security Services PTY. LTD.

Ive just had my logo made and I'm looking for some simple but strong designs for my business cards the company is a security company.

Please use dark colors.

Regards,

Owen Deloit

Reason: Need more time for discussion with other directors

Industry/Entity Type

Security

Font styles to use
Sans Serif
Decorative

```html
<!DOCTYPE html>
<html lang="en">
<head>
<meta charset="utf-8">
<title>K&amp;R Security Services – Business Cards</title>
<link rel="stylesheet" href="https://fonts.googleapis.com/css2?family=Cinzel:wght@500;600&family=Open+Sans:wght@400;600;700&display=swap">
<style>
  :root {
    --backdrop: #e4e2df;
    --card-black: #0b0b0b;
    --card-charcoal: #2a2a2a;
    --panel-light: #b9b9b9;
    --panel-mid: #8d8d8d;
    --panel-dark: #575757;
    --ink-dark: #1c1c1c;
    --ink-soft: #3a3a3a;
    --ink-pale: #d6d6d6;
    --band: #1e1e1e;
    --rule: #f0f0f0;
  }
  * { box-sizing: border-box; margin: 0; padding: 0; }
  html, body { width: 1200px; height: 800px; overflow: hidden; }
  body {
    background: var(--backdrop);
    font-family: "Open Sans", Arial, sans-serif;
    position: relative;
  }

  .card {
    position: absolute;
    width: 330px;
    height: 540px;
    top: 130px;
    border-radius: 4px;
    overflow: hidden;
    box-shadow: 0 14px 30px rgba(0,0,0,.28);
  }

  /* ---------- Back card ---------- */
  .card--back {
    left: 190px;
    background: radial-gradient(circle at 55% 45%, #3a3a3a 0%, #151515 45%, var(--card-black) 80%);
  }
  .back__site {
    position: absolute;
    left: 36px;
    top: 50%;
    transform: translate(-50%, -50%) rotate(90deg);
    font-size: 13px;
    letter-spacing: 4px;
    color: var(--ink-pale);
    white-space: nowrap;
  }
  .back__brand {
    position: absolute;
    left: 50%;
    top: 50%;
    transform: translate(-50%, -50%) rotate(90deg);
    display: flex;
    align-items: center;
    gap: 12px;
    white-space: nowrap;
  }
  .brand-name {
    font-family: "Cinzel", Georgia, serif;
    font-weight: 600;
    color: var(--ink-pale);
    font-size: 30px;
    letter-spacing: 2px;
  }
  .brand-dot {
    width: 16px; height: 16px;
    border-radius: 50%;
    background: var(--ink-pale);
  }

  /* ---------- Front card ---------- */
  .card--front {
    left: 680px;
    background: var(--card-charcoal);
  }
  .front__layout {
    position: absolute;
    width: 540px;
    height: 330px;
    left: 50%;
    top: 50%;
    transform: translate(-50%, -50%) rotate(-90deg);
  }
  .front__panel {
    position: absolute;
    left: 16px; top: 16px; right: 16px; bottom: 62px;
    background: linear-gradient(160deg, var(--panel-light) 0%, var(--panel-light) 50%, var(--panel-mid) 50.2%, var(--panel-dark) 100%);
    border: 1px solid #444;
  }
  .front__brand {
    position: absolute;
    right: 28px;
    top: 50px;
    display: flex;
    align-items: center;
    gap: 10px;
  }
  .front__brand .brand-name { color: var(--ink-dark); font-size: 26px; }
  .front__brand .brand-dot { background: var(--ink-dark); width: 14px; height: 14px; }

  .front__identity {
    position: absolute;
    left: 180px;
    top: 100px;
  }
  .person-name {
    font-family: "Cinzel", Georgia, serif;
    font-weight: 500;
    font-size: 27px;
    color: var(--ink-dark);
    letter-spacing: 1px;
  }
  .person-title {
    font-size: 12px;
    letter-spacing: 1px;
    color: var(--ink-dark);
    text-align: right;
  }

  .contacts {
    position: absolute;
    left: 30px;
    top: 160px;
    display: grid;
    grid-template-columns: auto auto;
    column-gap: 34px;
    row-gap: 10px;
    font-size: 13px;
    color: var(--ink-pale);
  }
  .contact {
    display: flex;
    align-items: center;
    gap: 8px;
    white-space: nowrap;
  }
  .contact--dark { color: var(--ink-dark); }
  .contact__icon {
    width: 18px; height: 18px;
    border-radius: 50%;
    background: var(--ink-soft);
    display: flex; align-items: center; justify-content: center;
  }
  .contact__icon svg { width: 11px; height: 11px; fill: var(--ink-pale); }

  .front__rule {
    position: absolute;
    left: 16px; right: 0;
    bottom: 56px;
    height: 2px;
    background: var(--rule);
  }
  .front__band {
    position: absolute;
    left: 0; right: 0; bottom: 0;
    height: 50px;
    background: var(--band);
    display: flex;
    align-items: center;
    padding-left: 32px;
    font-weight: 700;
    font-size: 14px;
    color: var(--rule);
    letter-spacing: .5px;
  }
  .front__band-tab {
    position: absolute;
    right: 0; bottom: 62px;
    width: 70px; height: 36px;
    background: var(--panel-mid);
  }
</style>
</head>
<body>

  <section class="card card--back" aria-label="Business card back">
    <p class="back__site">www.krsecurity.net.au</p>
    <div class="back__brand">
      <span class="brand-dot"></span>
      <span class="brand-name">K&amp;R SECURITY</span>
    </div>
  </section>

  <section class="card card--front" aria-label="Business card front">
    <div class="front__layout">
      <div class="front__panel">
        <div class="front__brand">
          <span class="brand-dot"></span>
          <span class="brand-name">K&amp;R SECURITY</span>
        </div>

        <div class="front__identity">
          <h1 class="person-name">DANIEL HART</h1>
          <p class="person-title">DIRECTOR</p>
        </div>

        <div class="contacts">
          <span></span>
          <span class="contact contact--dark">
            <span class="contact__icon"><svg viewBox="0 0 24 24"><path d="M6.6 10.8a15.1 15.1 0 0 0 6.6 6.6l2.2-2.2c.3-.3.7-.4 1-.2 1.1.4 2.3.6 3.6.6.6 0 1 .4 1 1V20c0 .6-.4 1-1 1A17 17 0 0 1 3 4c0-.6.4-1 1-1h3.5c.6 0 1 .4 1 1 0 1.3.2 2.5.6 3.6.1.3 0 .7-.2 1z"/></svg></span>
            (03) 95550148
          </span>
          <span class="contact">
            <span class="contact__icon"><svg viewBox="0 0 24 24"><rect x="6" y="2" width="12" height="20" rx="2"/></svg></span>
            0491555203
          </span>
          <span class="contact contact--dark">
            <span class="contact__icon"><svg viewBox="0 0 24 24"><path d="M2 5h20v14H2z M2 5l10 8 10-8"/></svg></span>
            kr@krsecurity.net.au
          </span>
          <span class="contact">owen@krsecurity.net.au</span>
        </div>
      </div>

      <div class="front__band-tab"></div>
      <div class="front__rule"></div>
      <div class="front__band">P.O. BOX 48 ELMWOOD VICTORIA 3131</div>
    </div>
  </section>

</body>
</html>
```